We need a website design for an HVAC (Heating & Air Conditioning) Contractor*

Our HVAC client would like to have a more professional looking site as their current one (https://brisvanecomfortworks.example/) is a template site. We will be building the site in-house from the concept.
Items we'd like to incorporate:
- A banner on the homepage that has a click to call plus a form on the right side of the banner
- There is a video on the current website homepage, please find a place to incorporate this.
- We will need to have at least 800 words of content on the homepage, please find space for that (can be a description of a few of the heating / air conditioning services they do). Feel free to use filler content (lorem ipsum) if need be to just show how the content would look

All submissions must have a homepage and a related subpage concept.

Number of Pages Required

1 page

```html
<!DOCTYPE html>
<html lang="en">
<head>
<meta charset="utf-8">
<title>Brisvane Comfort Works — Heating &amp; Air Conditioning</title>
<link href="https://fonts.googleapis.com/css2?family=Montserrat:ital,wght@0,400;0,500;0,600;0,700;1,400&family=Playfair+Display:wght@700&display=swap" rel="stylesheet">
<style>
:root{
  --navy:#163a6b;
  --navy-dark:#0f2c55;
  --red:#d40b0b;
  --ink:#1d1d1f;
  --muted:#5b5b60;
  --paper:#f3f3f4;
  --field:#eeeeef;
  --dark:#2a2a2c;
}
*{box-sizing:border-box;margin:0;padding:0}
html,body{width:1200px;height:3626px;overflow:hidden}
body{position:relative;background:var(--paper);font-family:"Montserrat",sans-serif;color:var(--ink)}
.abs{position:absolute}
.serif{font-family:"Playfair Display",serif;font-weight:700}
.btn{position:absolute;display:flex;align-items:center;justify-content:center;border-radius:20px;color:#fff;font-size:13px;font-weight:500}
.btn-red{background:var(--red)}
.btn-navy{background:var(--navy)}

/* top bar + header */
.header{left:0;top:0;width:1200px;height:120px;background:#fff}
.topbar{left:696px;top:0;width:504px;height:31px;background:var(--navy);clip-path:polygon(28px 0,100% 0,100% 100%,0 100%);color:#fff;font-size:12px;display:flex;align-items:center;justify-content:flex-end;padding-right:88px;gap:14px}
.brand{display:flex;align-items:center;gap:10px}
.brand-mark{width:22px;height:22px;background:var(--red)}
.brand-name{font-size:21px;font-weight:700;color:var(--red);line-height:1.1}
.nav{left:372px;top:67px;display:flex;gap:40px;font-size:13px;color:var(--ink)}
.nav .active{color:var(--red)}

/* hero */
.hero-bg{left:0;top:120px;width:1200px;height:700px;clip-path:polygon(0 0,100% 0,100% 520px,0 695px);background:linear-gradient(120deg,#8a8580 0%,#6d6a67 45%,#9b9894 100%)}
.hero-shade{left:0;top:120px;width:1200px;height:700px;clip-path:polygon(0 0,100% 0,100% 520px,0 695px);background:linear-gradient(90deg,rgba(30,30,30,.55),rgba(30,30,30,.1) 70%)}
.hero-title{left:88px;top:276px;width:620px;font-size:40px;line-height:1;color:#fff}
.hero-sub{left:88px;top:374px;width:680px;font-size:17px;line-height:1.25;color:#fff}
.form-frame{left:823px;top:196px;width:289px;height:367px;background:rgba(255,255,255,.35)}
.form-card{left:840px;top:212px;width:256px;height:335px;background:#fff}
.form-head{left:840px;top:212px;width:256px;height:80px;background:var(--navy);clip-path:polygon(0 0,100% 0,100% 62%,50% 100%,0 62%);color:#fff;font-size:15px;font-weight:600;text-align:center;padding-top:14px;line-height:1.25}
.field{position:absolute;left:856px;width:224px;height:32px;background:var(--field);font-size:12px;color:#555;display:flex;align-items:center;padding-left:14px}
.card{position:absolute;top:640px;width:232px;height:200px}
.card-label{position:absolute;left:0;bottom:0;width:100%;height:32px;background:var(--navy);clip-path:polygon(0 0,85% 0,100% 100%,0 100%);color:#fff;font-size:14px;font-weight:600;padding:8px 0 0 15px}

/* about */
.about-box{left:208px;top:920px;width:480px;height:480px;background:var(--red);color:#fff;padding:46px 48px}
.about-box h2{font-size:30px;line-height:1.15}
.about-lead{font-size:13px;font-weight:700;line-height:1.35;margin-top:32px}
.about-text{font-size:11.5px;line-height:1.66;margin-top:26px}
.about-photo{left:688px;top:997px;width:304px;height:480px;background:linear-gradient(160deg,#c9ccd2,#8b8f98 55%,#b8a48a)}

/* trust */
.trust-title{left:0;width:1200px;top:1548px;text-align:center;font-size:32px;line-height:1.18;color:var(--navy)}
.feature{position:absolute;top:1652px;width:220px;text-align:center;font-size:15px;line-height:1.3;color:var(--ink)}
.feature svg{display:block;margin:0 auto 18px}

/* video + testimonial */
.dark-band{left:0;top:2070px;width:1200px;height:950px;background:linear-gradient(180deg,#3a3a3c,#232325);clip-path:polygon(0 160px,100% 0,100% 800px,0 948px)}
.video{left:208px;top:1951px;width:784px;height:336px;background:linear-gradient(100deg,#8d7a6a 0%,#7e7470 40%,#5c6066 70%,#7a7f87 100%)}
.clients-title{left:0;width:1200px;top:2352px;text-align:center;font-size:32px;color:#fff}
.avatar{left:557px;top:2426px;width:80px;height:80px;border-radius:50%;background:linear-gradient(160deg,#f0d6b4,#c99a6e);border:3px solid #fff}
.quote{left:270px;top:2524px;width:660px;text-align:center;font-size:14.5px;font-style:italic;line-height:1.65;color:#fff}
.rule{top:2652px;height:1px;background:rgba(255,255,255,.6)}
.dots{left:564px;top:2752px;display:flex;gap:5px}
.dots span{width:9px;height:9px;border-radius:50%;border:1px solid #fff}
.dots .on{background:#fff;box-shadow:inset 0 0 0 2px #333}

/* booking */
.book-back{left:128px;top:2876px;width:456px;height:332px;background:var(--red);border-radius:0 0 0 26px}
.book-photo{left:88px;top:2866px;width:480px;height:326px;background:linear-gradient(120deg,#a9b58a,#e3ddd2 45%,#c9c0b4);border-radius:0 0 0 26px}
.book-title{right:87px;top:3060px;font-size:25px;color:var(--ink)}
.book-call{right:87px;top:3096px;font-size:40px;font-weight:500;color:var(--navy)}

/* footer */
.footer{left:0;top:3272px;width:1200px;height:354px;background:var(--navy);color:#fff}
.foot-head{position:absolute;top:3352px;font-size:17px;font-weight:600;color:#fff}
.foot-text{position:absolute;font-size:12px;line-height:1.6;color:#fff}
.news{left:878px;top:3444px;width:234px;height:32px;background:#fff;border-radius:16px;font-size:11px;color:#666;padding:9px 14px}
.news-go{left:1083px;top:3450px;width:21px;height:21px}
.foot-rule{left:88px;top:3536px;width:1024px;height:1px;background:rgba(255,255,255,.3)}
.social{position:absolute;top:3566px;width:26px;height:26px;border-radius:50%;border:1px solid var(--red)}
.badge{position:absolute;top:3560px;width:46px;height:46px}
</style>
</head>
<body>

<!-- header -->
<div class="abs header"></div>
<div class="abs topbar"><span>Call Us: (555) 014-2290</span><span>|</span><span>Email: hello@brisvanecomfort.example</span></div>
<div class="abs brand" style="left:88px;top:52px"><span class="brand-mark"></span><span class="brand-name">Brisvane<br>Comfort Works</span></div>
<nav class="abs nav">
  <span class="active">Home</span><span>About Us</span><span>Services &#8964;</span><span>Reviews</span><span>Specials</span><span>Contact Us</span>
</nav>
<div class="btn btn-red" style="left:952px;top:60px;width:160px;height:31px">Services Request</div>

<!-- hero -->
<div class="abs hero-bg" role="img" aria-label="Woman relaxing on a sofa beneath a wall air conditioner in a bright living room"></div>
<div class="abs hero-shade"></div>
<h1 class="abs serif hero-title">Keep Your Friends and Family Comfortable</h1>
<p class="abs hero-sub">Look To The Professionals To Take Care Of All Hvac Services In Kelmont, Ridgefalls, Ok &amp; Surrounding Areas</p>
<div class="btn btn-red" style="left:88px;top:445px;width:144px;height:30px;font-size:12.5px">Contact Us Today!</div>

<div class="abs form-frame"></div>
<div class="abs form-card"></div>
<div class="abs form-head">Schedule Your Appointment<br>Today</div>
<div class="field" style="top:301px">Name</div>
<div class="field" style="top:350px">Email</div>
<div class="field" style="top:400px">Phone No.</div>
<div class="field" style="top:449px">Services<span style="position:absolute;right:14px">&#8964;</span></div>
<div class="btn btn-red" style="left:912px;top:499px;width:112px;height:30px">Submit</div>

<div class="card" style="left:88px;background:linear-gradient(160deg,#dfe3e8,#9aa3ad 60%,#5d5a4d)" role="img" aria-label="Geothermal steam rising from the ground"><div class="card-label">Geothermal</div></div>
<div class="card" style="left:352px;background:linear-gradient(160deg,#d6d7d9,#8fa7a2 50%,#c9a23a)" role="img" aria-label="Technician holding HVAC pressure gauges"><div class="card-label">Residential HVAC</div></div>
<div class="card" style="left:616px;background:linear-gradient(160deg,#e6e6e6,#7b7e83 55%,#3e4046)" role="img" aria-label="Rooftop commercial condenser fans"><div class="card-label">Commercial HVAC</div></div>
<div class="card" style="left:879px;background:linear-gradient(160deg,#7f9a6a,#a7a9ab 50%,#8a4d36)" role="img" aria-label="Outdoor air conditioning units beside a house"><div class="card-label">Maintenance Plan</div></div>

<!-- about -->
<div class="abs about-box">
  <h2 class="serif">Go the Energy-Efficient Route</h2>
  <p class="about-lead">Make sure you hire an experienced hvac company in kelmont &amp; ridgefalls, ok</p>
  <p class="about-text">Brisvane Comfort Works, LLC provides a wide variety of residential and commercial HVAC services in the Kelmont, OK area. With over a decade of experience, you can trust our HVAC company to install, repair and maintain the HVAC systems in your home or commercial building. Our technician can find out what's wrong with your malfunctioning heating or cooling system and repair or replace it on the spot. We specialize in energy-efficient geothermal heating and cooling systems ...</p>
</div>
<div class="btn btn-navy" style="left:256px;top:1322px;width:128px;height:30px">About Us</div>
<div class="abs about-photo" role="img" aria-label="Technician checking an outdoor air conditioning unit with gauges"></div>

<!-- trust -->
<h2 class="abs serif trust-title">See Why Customers Trust Brisvane<br>Comfort Works</h2>
<div class="feature" style="left:94px">
  <svg width="56" height="66" viewBox="0 0 56 66" fill="none" stroke-width="2.5"><circle cx="28" cy="24" r="20" stroke="#163a6b"/><circle cx="28" cy="24" r="13" stroke="#d40b0b"/><path d="M28 16l2.5 5 5.5.8-4 3.9 1 5.5-5-2.6-5 2.6 1-5.5-4-3.9 5.5-.8z" stroke="#d40b0b"/><path d="M16 40l-6 20 9-4 5 8 4-14M40 40l6 20-9-4-5 8-4-14" stroke="#163a6b"/></svg>
  We have over 10 years of heating and cooling experience
</div>
<div class="feature" style="left:358px">
  <svg width="60" height="66" viewBox="0 0 60 66" fill="none" stroke-width="2.5"><rect x="6" y="4" width="40" height="56" rx="2" stroke="#163a6b"/><path d="M14 16h24M14 24h24M14 32h16" stroke="#163a6b"/><path d="M14 46l4 4 8-8" stroke="#d40b0b"/><path d="M54 22L34 48l-6 4 2-7 20-26z" stroke="#d40b0b"/></svg>
  We offer free<br>HVAC replacement estimates
</div>
<div class="feature" style="left:622px">
  <svg width="66" height="66" viewBox="0 0 66 66" fill="none" stroke-width="2.5"><path d="M33 4v58" stroke="#163a6b"/><path d="M33 14a19 19 0 0 0 0 38" stroke="#d40b0b"/><path d="M40 14l8-6M40 52l8 6M45 33h16M45 20l10-6M45 46l10 6M33 10l-5-5M33 10l5-5M33 56l-5 5M33 56l5 5" stroke="#163a6b"/></svg>
  We provide residential and commercial HVAC services
</div>
<div class="feature" style="left:886px">
  <svg width="66" height="66" viewBox="0 0 66 66" fill="none" stroke-width="2.5"><path d="M10 56L44 22M44 22a10 10 0 1 0 12-12l-7 7-5-1-1-5 7-7a10 10 0 0 0-12 12" stroke="#163a6b"/><path d="M8 8l4-2 28 28-4 4L8 12z" stroke="#163a6b"/><path d="M36 40l16 16a4 4 0 0 0 5-5L41 35" stroke="#d40b0b"/></svg>
  We offer HVAC mainte-<br>nance plans
</div>
<div class="btn btn-red" style="left:328px;top:1834px;width:263px;height:30px">Schedule Your Appointment Today</div>
<div class="btn btn-navy" style="left:609px;top:1834px;width:263px;height:30px">Contact for Emergency Services</div>

<!-- video + testimonials -->
<div class="abs dark-band" role="img" aria-label="Faded black and white family photo background"></div>
<div class="abs video" role="img" aria-label="Video: technician servicing an outdoor condenser unit"></div>
<svg class="abs" style="left:576px;top:2096px" width="48" height="48" viewBox="0 0 48 48" fill="none"><circle cx="24" cy="24" r="21" stroke="#fff" stroke-width="3"/><path d="M19 14l14 10-14 10z" stroke="#fff" stroke-width="3" stroke-linejoin="round"/></svg>

<h2 class="abs serif clients-title">Happy Clients Say</h2>
<div class="abs avatar" role="img" aria-label="Client portrait"></div>
<p class="abs quote">Lorem ipsum dolor sit amet, consectetur adipisicing elit, sed do eiusmod tempor incididunt ut labore et dolore magna aliqua. Ut enim ad minim veniam, quis nostrud exercitation ullamco laboris nisi ut aliquip ex ea commodo consequat. Duis aute irure dolor in reprehenderit.</p>
<div class="abs rule" style="left:436px;width:140px"></div>
<div class="abs" style="left:586px;top:2640px;font-size:20px;color:var(--red);font-family:'Playfair Display',serif">&#8220;</div>
<div class="abs rule" style="left:618px;width:140px"></div>
<div class="abs" style="left:0;width:1192px;top:2670px;text-align:center;font-size:14px;color:var(--red)">Jordan Ellery</div>
<div class="abs" style="left:0;width:1192px;top:2692px;text-align:center;font-size:12px;color:#fff">Lorem Site</div>
<div class="abs dots"><span></span><span class="on"></span><span></span><span></span><span></span></div>

<!-- booking -->
<div class="abs book-back"></div>
<div class="abs book-photo" role="img" aria-label="Smiling woman on a sofa using her phone"></div>
<svg class="abs" style="left:1048px;top:2962px" width="64" height="62" viewBox="0 0 64 62" fill="none" stroke="#163a6b" stroke-width="2.5"><rect x="3" y="8" width="58" height="50" rx="4"/><path d="M3 20h58M16 3v10M48 3v10"/><g stroke="#d40b0b"><circle cx="16" cy="30" r="3"/><circle cx="28" cy="30" r="3"/><circle cx="40" cy="30" r="3"/><circle cx="52" cy="30" r="3"/><circle cx="28" cy="42" r="3"/><circle cx="40" cy="42" r="3"/><circle cx="52" cy="42" r="3"/></g><circle cx="15" cy="46" r="7"/><path d="M11 46l3 3 5-5"/></svg>
<div class="abs book-title">Book Your Appointment</div>
<div class="abs book-call">Call:&nbsp; (555) 014-2290</div>
<div class="btn btn-red" style="left:914px;top:3153px;width:199px;height:38px;font-size:12.5px">Book Your Appointment</div>

<!-- footer -->
<div class="abs footer"></div>
<div class="abs brand" style="left:88px;top:3368px"><span class="brand-mark"></span><span class="brand-name" style="color:#fff">Brisvane<br>Comfort Works</span></div>

<div class="foot-head" style="left:352px">Contact Us</div>
<div class="foot-text" style="left:352px;top:3384px;font-size:15px"><span style="color:var(--red)">Call Us:</span> (555) 014-2290</div>
<div class="foot-text" style="left:352px;top:3408px"><span style="color:var(--red)">e:</span> hello@brisvanecomfort.example</div>
<div class="foot-text" style="left:352px;top:3448px">Brisvane Comfort Works, Llc<br>KELMONT, OK 70010</div>

<div class="foot-head" style="left:615px">Quick Links</div>
<div class="foot-text" style="left:615px;top:3386px">Home<br>About Us<br>Services<br>Reviews<br>Specials</div>
<div class="foot-text" style="left:702px;top:3386px">Home Financing<br>Contact Us</div>

<div class="foot-head" style="left:878px">Sign Up Newsletter</div>
<div class="foot-text" style="left:878px;top:3386px">There are many variations of passages<br>lorem Ipsum available</div>
<div class="abs news">Enter your email ...</div>
<svg class="abs news-go" viewBox="0 0 21 21"><circle cx="10.5" cy="10.5" r="10.5" fill="#d40b0b"/><path d="M6 6l10 4.5L6 15l2-4.5z" fill="#fff"/></svg>

<div class="abs foot-rule"></div>
<div class="foot-text" style="left:88px;top:3572px">© 2021 <span style="color:var(--red)">Brisvane Comfort Works, LLC</span> All Right Reserved</div>
<div class="social" style="left:618px"></div>
<div class="social" style="left:656px;background:var(--red)"></div>
<div class="social" style="left:694px"></div>
<div class="social" style="left:732px"></div>
<div class="badge" style="left:880px;background:#e8a23a;border-radius:4px"></div>
<div class="badge" style="left:938px;background:#c8ccd3;border-radius:50%"></div>
<div class="badge" style="left:1004px;background:#e07a2c;border-radius:6px"></div>
</body>
</html>
```